Pella Acupuncture Business Card Design

I would like a business card design for my acupuncture business which is based from 2 practices in Melbourne, Australia.

The front of the card should include:

*The Logo
* Name - Miranda Tovelisca (B.App.Sc.(TCM), Dip.Rem.Mass.). (I would like the letters after my name in slightly smaller font)
* Mobile number - 0472 318 604
* Web address - www.pellaacupuncture-example.com.au

On the back of the card I would somehow like to fit my 2 clinic addresses in. They are:

The Birchwood Restoration Rooms
842 Fennimore Rd, Camberwell VIC 3124
Ph: 1300 274 518

Quillbrook Integrative & Eastern Herbal Therapy Clinic
31 Marlowby Rd, Malvern East VIC 3145
Ph: (03) 9871 3352

If there is space, I'd also like to add to the back of the card - Next Appointment............................ (or something along those lines).

Thanks and happy designing!

Target Market(s)

Health consumers, and colleagues in the health industry

Industry/Entity Type

Clinic

Contact Information for Business Card

as above in brief

Requirements
Must have
• I've seen some ok designs coming in, however I'd like to avoid the generic look with the added curved line details etc. I don't particularly need extra patterns added to the card. I'd prefer it to look quite clean and simple, and using more earthy colours (I'm not super keen on the lime green that a lot of designs seem to include. I don't mind the full black or white look, (obviously the back side needs to be a lighter colour to allow me to write appointment details on it). I also quite like the idea of the background looking like brown recycled paper (just an idea - that's not 100% necessary).
Nice to have
• I have an idea that I could have the main flower part of the logo printed as metallic.
Should not have
• Generic patterns and too much added detail.

```html
<!DOCTYPE html>
<html lang="en">
<head>
<meta charset="utf-8">
<title>Pella Acupuncture — Business Card</title>
<link href="https://fonts.googleapis.com/css2?family=Lato:wght@400;700;900&family=Montserrat:wght@700;800&display=swap" rel="stylesheet">
<style>
  :root {
    --stage: #2b2b2b;
    --card: #fbfbfa;
    --ink: #1c1c1c;
    --ink-soft: #3a3a3a;
    --muted: #9a9a9a;
    --leaf: #4cae4c;
    --olive: #8a9a3a;
    --sand: #d8cfa6;
    --mint: #cfe9c4;
    --pill: #262626;
  }
  * { box-sizing: border-box; margin: 0; padding: 0; }
  html, body { width: 1200px; height: 997px; overflow: hidden; }
  body {
    background: var(--stage);
    position: relative;
    font-family: "Lato", sans-serif;
    color: var(--ink);
  }
  .card {
    position: absolute;
    width: 540px;
    height: 330px;
    background: var(--card);
    border-radius: 26px;
    overflow: hidden;
    box-shadow: 0 18px 40px rgba(0,0,0,.45);
  }
  .card--back { left: 90px; top: 100px; }
  .card--front { left: 570px; top: 540px; }

  .motif {
    position: absolute;
    left: -90px;
    bottom: -70px;
    width: 300px;
    height: 300px;
    border-radius: 50%;
    background: radial-gradient(circle at 50% 50%, rgba(255,255,255,1) 0 30%, rgba(176,222,200,.55) 38%, rgba(216,207,166,.45) 55%, rgba(216,207,166,0) 72%);
  }

  /* back */
  .addresses { position: absolute; left: 250px; top: 22px; width: 270px; }
  .addresses__title {
    display: inline-block;
    background: var(--pill);
    color: var(--leaf);
    font-weight: 900;
    font-size: 13px;
    letter-spacing: .5px;
    padding: 4px 12px;
    border-radius: 12px;
    margin-bottom: 8px;
  }
  .clinic { margin-bottom: 10px; }
  .clinic__name {
    color: var(--leaf);
    font-weight: 900;
    font-size: 12px;
    line-height: 1.2;
    text-transform: uppercase;
    margin-bottom: 3px;
  }
  .contact-row {
    display: flex;
    align-items: center;
    gap: 7px;
    font-size: 12px;
    color: var(--ink-soft);
    margin-top: 3px;
  }
  .icon-dot {
    width: 17px; height: 17px; border-radius: 50%;
    background: var(--ink-soft);
    display: flex; align-items: center; justify-content: center;
    flex: none;
  }
  .appointment {
    position: absolute;
    left: 150px; right: 30px; top: 250px;
    font-size: 12px;
    font-weight: 700;
    color: var(--muted);
    text-align: center;
  }
  .rule-top {
    position: absolute; left: 250px; right: 28px; top: 205px;
    height: 2px; background: var(--ink-soft);
  }
  .rule-bottom {
    position: absolute; left: 150px; right: 30px; top: 290px;
    height: 2px; background: var(--ink-soft);
  }

  /* front */
  .brand {
    position: absolute; right: 34px; top: 40px;
    display: flex; align-items: center; gap: 12px;
  }
  .brand__dot { width: 46px; height: 46px; border-radius: 50%; background: var(--ink); }
  .brand__name {
    font-family: "Lato", sans-serif;
    font-weight: 900;
    font-size: 22px;
    color: var(--ink);
  }
  .accent-line {
    position: absolute; right: 24px; top: 175px; width: 360px; height: 3px;
    background: linear-gradient(90deg, var(--sand), var(--leaf));
  }
  .identity { position: absolute; left: 26px; top: 188px; }
  .identity__name {
    font-family: "Montserrat", sans-serif;
    font-weight: 800;
    font-size: 22px;
    letter-spacing: .3px;
    color: var(--ink);
  }
  .identity__creds {
    font-family: "Montserrat", sans-serif;
    font-weight: 700;
    font-size: 14px;
    color: var(--olive);
    margin-top: 2px;
  }
  .front-contacts { position: absolute; left: 26px; top: 256px; }
  .front-contacts .contact-row { font-size: 15px; font-weight: 900; color: var(--ink); margin-top: 7px; gap: 10px; }
  .front-contacts .icon-dot { width: 22px; height: 22px; background: var(--ink); }
</style>
</head>
<body>

<section class="card card--back" aria-label="Card back">
  <div class="motif" role="img" aria-label="Faint decorative flower motif"></div>
  <div class="addresses">
    <div class="addresses__title">CLINIC ADDRESSES:</div>
    <div class="clinic">
      <div class="clinic__name">The Birchwood Restoration Rooms</div>
      <div class="contact-row">
        <span class="icon-dot"><svg width="11" height="11" viewBox="0 0 12 12"><path d="M6 1 1 6h2v5h2.5V8h1v3H9V6h2z" fill="#fff"/></svg></span>
        842 Fennimore Rd, Camberwell, VIC 3124
      </div>
      <div class="contact-row">
        <span class="icon-dot"><svg width="11" height="11" viewBox="0 0 12 12"><path d="M3 1.5 4.6 3.6 3.8 5c.7 1.4 1.8 2.5 3.2 3.2l1.4-.8 2.1 1.6-.9 1.6C6 10.4 1.6 6 1.4 2.4z" fill="#fff"/></svg></span>
        1300 274 518
      </div>
    </div>
    <div class="clinic">
      <div class="clinic__name">Quillbrook Integrative &amp; Eastern Herbal Therapy Clinic</div>
      <div class="contact-row">
        <span class="icon-dot"><svg width="11" height="11" viewBox="0 0 12 12"><path d="M6 1 1 6h2v5h2.5V8h1v3H9V6h2z" fill="#fff"/></svg></span>
        31 Marlowby Rd, Malvern East, VIC 3145
      </div>
      <div class="contact-row">
        <span class="icon-dot"><svg width="11" height="11" viewBox="0 0 12 12"><path d="M3 1.5 4.6 3.6 3.8 5c.7 1.4 1.8 2.5 3.2 3.2l1.4-.8 2.1 1.6-.9 1.6C6 10.4 1.6 6 1.4 2.4z" fill="#fff"/></svg></span>
        (03) 9871 3352
      </div>
    </div>
  </div>
  <div class="rule-top"></div>
  <div class="appointment">Next Appointment</div>
  <div class="rule-bottom"></div>
</section>

<section class="card card--front" aria-label="Card front">
  <div class="motif" role="img" aria-label="Faint decorative flower motif"></div>
  <div class="brand">
    <span class="brand__dot"></span>
    <span class="brand__name">Pella Acupuncture</span>
  </div>
  <div class="accent-line"></div>
  <div class="identity">
    <div class="identity__name">MIRANDA TOVELISCA</div>
    <div class="identity__creds">B.APP.SC.(TCM), DIP.REM.MASS</div>
  </div>
  <div class="front-contacts">
    <div class="contact-row">
      <span class="icon-dot"><svg width="13" height="13" viewBox="0 0 12 12"><path d="M3 1.5 4.6 3.6 3.8 5c.7 1.4 1.8 2.5 3.2 3.2l1.4-.8 2.1 1.6-.9 1.6C6 10.4 1.6 6 1.4 2.4z" fill="#fff"/></svg></span>
      0472 318 604
    </div>
    <div class="contact-row">
      <span class="icon-dot"><svg width="13" height="13" viewBox="0 0 12 12"><rect x="1" y="2.5" width="10" height="7" fill="none" stroke="#fff" stroke-width="1.2"/><path d="M1 2.5 6 6.5l5-4" fill="none" stroke="#fff" stroke-width="1.2"/></svg></span>
      www.pellaacupuncture-example.com.au
    </div>
  </div>
</section>

</body>
</html>
```